New web design needed for our company

We need our website designing, it needs to be professional and look creative,
We are a plumbing and heating company called Brackwell Flow's (www.brackwellflows.co.uk)
I like this site design also some of the following maybe:
https://www.tindermoorwarmth.com/
http://www.quorvapower.co.uk

Please let me know when you want our logo files as it wont let me upload them

The design will require coding once the design is complete, i havent paid for this yet as i want to be sure the design is good before i commit.

The template needs to look professional and look like one of the leading companies.
The site will consist of all the features this site has https://www.tindermoorwarmth.com/

I like a modern design with the latest technology.

Must have a customer login page and a my account area

Target Market(s)

Everyone

Industry/Entity Type

Plumbing

Coding

Coded - Design and coding required

Number of Pages Required

5+ page

Font styles to use
Other font styles liked:
• whatever suites

Requirements
Must have
• The design will require coding once the design is complete, i havent paid for this yet as i want to be sure the design is good before i commit.
• The template needs to look professional and look like one of the leading companies.
• The site will consist of all the features this site has https://www.tindermoorwarmth.com/
• I like a modern design with the latest technology.
• Must have a customer login page and a my account area
Nice to have
• inspirational and different
Should not have
• plain boring designs like most plumbing websites, needs to be inspiring and attract people from first sight.

```html
<!DOCTYPE html>
<html lang="en">
<head>
<meta charset="utf-8">
<title>Brackwell Flow's – Plumbing &amp; Heating</title>
<link href="https://fonts.googleapis.com/css2?family=Open+Sans:ital,wght@0,300;0,400;0,600;0,700;1,400&display=swap" rel="stylesheet">
<style>
:root{
  --navy:#0c2d66;
  --navy-dark:#0b1c36;
  --navy-deeper:#081528;
  --orange:#ef4a23;
  --yellow:#f6ea2c;
  --ink:#222831;
  --muted:#6b7280;
  --topbar:#eef0f3;
  --svc-bg:#eef6fb;
  --news-bg:#f4f6f8;
  --line:#c9d3dc;
  --white:#ffffff;
}
*{box-sizing:border-box;margin:0;padding:0}
html,body{width:1200px;height:2410px;overflow:hidden}
body{position:relative;font-family:"Open Sans",sans-serif;color:var(--ink);background:var(--white)}
.abs{position:absolute}

.topbar{left:0;top:0;width:1200px;height:44px;background:var(--topbar);font-size:12px;color:#6d737b;text-transform:uppercase}
.topbar .tagline{left:80px;top:14px}
.topbar .hours{right:80px;top:14px}

.header{left:0;top:44px;width:1200px;height:104px;background:var(--white)}
.logo{left:77px;top:22px;display:flex;align-items:center;gap:8px}
.logo .dot{width:14px;height:14px;border-radius:50%;background:var(--orange)}
.logo .name{font-size:38px;font-weight:700;color:var(--navy);letter-spacing:-1px;line-height:1}
.logo-sub{left:200px;top:68px;font-size:11px;color:var(--navy)}
.contact{display:flex;align-items:center;gap:14px}
.contact .label{font-size:10px;color:#6d737b;text-transform:uppercase}
.contact .value{font-size:21px;color:#111;line-height:1.1}
.contact.phone{left:643px;top:30px}
.contact.phone .value{letter-spacing:4px;font-weight:600}
.contact.mail{left:936px;top:30px}
.header .divider{left:888px;top:26px;width:1px;height:46px;background:#bfc4ca}

.nav{left:0;top:148px;width:1200px;height:52px;background:var(--navy)}
.nav a{position:absolute;top:16px;font-size:15px;color:var(--white);text-decoration:none}
.nav a.active{color:var(--orange)}
.quote{left:935px;top:138px;width:176px;height:48px;background:var(--yellow);border-radius:0 0 40px 40px/0 0 14px 14px;font-size:12px;font-weight:700;color:#111;text-align:center;line-height:52px;text-transform:uppercase}

.hero{left:0;top:200px;width:1200px;height:413px;background:linear-gradient(90deg,#6fa2d8 0%,#b9d3ee 35%,#e9eef3 55%,#d9dde2 75%,#b8bcc1 100%)}
.hero-arrow{top:392px}

.section-title{display:flex;align-items:center;gap:14px;font-size:27px;font-weight:400;text-transform:uppercase;color:#111}

.services{left:0;top:613px;width:1200px;height:532px;background:var(--svc-bg)}
.svc-nav{width:30px;height:31px;border:2px solid var(--navy);display:flex;align-items:center;justify-content:center;background:var(--white)}
.svc-card{top:872px;width:281px;height:183px;border:1px solid var(--line);background:transparent}
.svc-photo{top:766px;width:225px;height:170px}
.svc-title{top:952px;width:281px;text-align:center;font-size:21px;font-weight:300;line-height:1.25;color:#222}
.btn-dark{background:var(--navy);color:var(--white);font-size:12px;text-transform:uppercase;text-align:center;display:flex;align-items:center;justify-content:center}
.svc-btn{top:1028px;width:119px;height:27px}

.about-text{left:145px;top:1266px;width:430px;font-size:19px;line-height:32px;color:#444}
.read-more{left:146px;top:1489px;width:131px;height:41px;border:2px solid var(--navy);border-radius:4px;font-size:17px;display:flex;align-items:center;justify-content:center;color:#111}
.testimonial{left:668px;top:1277px;width:450px;height:249px;background:var(--white);box-shadow:0 0 6px rgba(0,0,0,.15);overflow:hidden}
.testimonial .quote-text{position:absolute;left:37px;top:52px;width:255px;font-size:11px;font-style:italic;line-height:20px;color:#666}
.testimonial .who{position:absolute;left:37px;top:165px;font-size:12px;font-weight:700;color:#111;text-transform:uppercase}
.testimonial .role{position:absolute;left:37px;top:192px;font-size:10px;color:#666;text-transform:uppercase}
.testimonial .portrait{position:absolute;left:275px;top:0;width:175px;height:249px;border-radius:100% 0 0 0/100% 0 0 0;background:linear-gradient(160deg,#cfe9f4,#7fc4db 60%,#c8333d 100%)}

.news{left:0;top:1582px;width:1200px;height:450px;background:var(--news-bg)}
.view-all{left:1020px;top:1654px;width:95px;height:36px;border:2px solid var(--navy);background:var(--white);font-size:12px;font-weight:700;letter-spacing:1px;display:flex;align-items:center;justify-content:center;color:#111}
.news-card{top:1739px;width:260px;height:217px;background:var(--white);box-shadow:0 0 5px rgba(0,0,0,.08)}
.news-card .mark{position:absolute;left:0;top:38px;width:5px;height:14px;background:var(--navy)}
.news-card h3{position:absolute;left:26px;top:37px;font-size:13px;font-weight:700;text-transform:uppercase;color:#111}
.news-card .meta{position:absolute;left:26px;top:66px;font-size:10px;color:#666;text-transform:uppercase}
.news-card .meta span{color:var(--orange)}
.news-card p{position:absolute;left:26px;top:90px;width:215px;font-size:11px;line-height:19px;color:var(--orange)}
.news-card .btn-dark{position:absolute;left:26px;top:185px;width:98px;height:35px;font-size:11px}
.news-photo{top:1715px;width:249px;height:267px}

.footer{left:0;top:2060px;width:1200px;height:285px;background:var(--navy-dark);color:var(--white)}
.foot-col{top:2113px}
.foot-col h4{font-size:13px;font-weight:600;text-transform:uppercase;letter-spacing:.3px}
.foot-col .rule{width:56px;height:2px;background:#9aa6b8;margin:16px 0 18px}
.foot-col ul{list-style:none}
.foot-col li{font-size:13px;height:31.7px;color:#e6e9ee}
.foot-col li.hl{color:var(--orange)}
.socials{left:922px;top:2284px;display:flex;gap:16px;align-items:center}
.socials span{width:14px;height:14px;border-radius:50%;background:#e6e9ee}
.socials span:first-child{background:var(--orange)}
.copyright{left:0;top:2345px;width:1200px;height:65px;background:var(--navy-deeper);color:var(--white);font-size:13px;font-weight:600;display:flex;align-items:center;justify-content:center}
</style>
</head>
<body>

<svg width="0" height="0" style="position:absolute">
  <defs>
    <symbol id="tap" viewBox="0 0 30 34">
      <rect x="2" y="6" width="8" height="12" fill="#ef4a23"/>
      <rect x="8" y="9" width="14" height="7" fill="#ef4a23"/>
      <rect x="12" y="3" width="6" height="6" fill="#ef4a23"/>
      <rect x="8" y="1" width="14" height="3" fill="#ef4a23"/>
      <rect x="20" y="9" width="6" height="12" fill="#ef4a23"/>
      <path d="M23 24c-2 3-2 5 0 6 2-1 2-3 0-6z" fill="#ef4a23"/>
    </symbol>
  </defs>
</svg>

<div class="abs topbar">
  <span class="abs tagline">Best plumbing company website forever!</span>
  <span class="abs hours">Working hours : Mon-Sat (8.00am - 6.00pm)</span>
</div>

<header class="abs header">
  <div class="abs logo"><span class="dot"></span><span class="name">Brackwell Flow's</span></div>
  <span class="abs logo-sub">Your Local Experts</span>
  <div class="abs contact phone">
    <svg width="24" height="24" viewBox="0 0 24 24"><path d="M6.6 10.8c1.4 2.8 3.8 5.1 6.6 6.6l2.2-2.2c.3-.3.7-.4 1-.2 1.1.4 2.3.6 3.6.6.6 0 1 .4 1 1V20c0 .6-.4 1-1 1C10.6 21 3 13.4 3 4c0-.6.4-1 1-1h3.5c.6 0 1 .4 1 1 0 1.3.2 2.5.6 3.6.1.3 0 .7-.2 1z" fill="#ef4a23"/></svg>
    <div><div class="label">Call to schedule your free !</div><div class="value">08105577</div></div>
  </div>
  <div class="abs divider"></div>
  <div class="abs contact mail">
    <svg width="28" height="20" viewBox="0 0 28 20"><rect x="1" y="1" width="26" height="18" fill="none" stroke="#ef4a23" stroke-width="2"/><path d="M1 1l13 10L27 1" fill="none" stroke="#ef4a23" stroke-width="2"/></svg>
    <div><div class="label">Our email id</div><div class="value">abc@flowmail.com</div></div>
  </div>
</header>

<nav class="abs nav">
  <a class="active" href="#" style="left:80px">Home</a>
  <a href="#" style="left:175px">My Account</a>
  <a href="#" style="left:308px">Services</a>
  <a href="#" style="left:418px">Emergencies</a>
  <a href="#" style="left:557px">Business</a>
  <a href="#" style="left:671px">Customers</a>
</nav>
<div class="abs quote">Free instant quote</div>

<div class="abs hero" role="img" aria-label="Chrome bathroom tap beside a plumber's hands tightening pipe fittings with a red wrench"></div>
<svg class="abs hero-arrow" style="left:34px" width="16" height="28" viewBox="0 0 16 28"><path d="M14 2L3 14l11 12" fill="none" stroke="#5d6670" stroke-width="4"/></svg>
<svg class="abs hero-arrow" style="left:1124px" width="16" height="28" viewBox="0 0 16 28"><path d="M2 2l11 12L2 26" fill="none" stroke="#ffffff" stroke-width="4"/></svg>

<section class="abs services">
  <h2 class="abs section-title" style="left:100px;top:70px"><svg width="30" height="34"><use href="#tap"/></svg>Service we offer</h2>
  <div class="abs svc-nav" style="left:1046px;top:63px"><svg width="8" height="12" viewBox="0 0 8 12"><path d="M6 1L1 6l5 5" fill="none" stroke="#0c2d66" stroke-width="2"/></svg></div>
  <div class="abs svc-nav" style="left:1086px;top:63px"><svg width="8" height="12" viewBox="0 0 8 12"><path d="M2 1l5 5-5 5" fill="none" stroke="#0c2d66" stroke-width="2"/></svg></div>
</section>

<div class="abs svc-card" style="left:98px"></div>
<div class="abs svc-photo" role="img" aria-label="Engineer in blue overalls installing a system boiler" style="left:125px;background:linear-gradient(135deg,#2c4f9e,#c9ccd2 55%,#d2283a)"></div>
<div class="abs svc-title" style="left:98px">System<br>Boiler Installation</div>
<div class="abs svc-btn btn-dark" style="left:179px">View details</div>

<div class="abs svc-card" style="left:416px"></div>
<div class="abs svc-photo" role="img" aria-label="Plumber replacing a wall-mounted boiler" style="left:445px;background:linear-gradient(135deg,#f1f1f1,#c6c2bd 55%,#6d7a8c)"></div>
<div class="abs svc-title" style="left:416px;top:950px">Replace<br>a System Boiler</div>
<div class="abs svc-btn btn-dark" style="left:497px">View details</div>

<div class="abs svc-card" style="left:779px"></div>
<div class="abs svc-photo" role="img" aria-label="Blue gas flame ring on a hob burner" style="left:808px;background:radial-gradient(ellipse at 50% 60%,#2f8cff 0%,#0b3fa8 35%,#020612 75%)"></div>
<div class="abs svc-title" style="left:779px;top:955px">Gas Safety<br>Certificate (CP12)</div>
<div class="abs svc-btn btn-dark" style="left:860px">View details</div>

<h2 class="abs section-title" style="left:100px;top:1192px"><svg width="30" height="34"><use href="#tap"/></svg>About Brackwell Flow's</h2>
<p class="abs about-text">Lorem ipsum dolor sit amet, consectetur adipiscing elit. Suspendisse ornare magna erat, in molestie fe varius quis. Phasellus mattis neque in ex facilisis aliquam. Donec lacus ipsum, sodales id semper qu sfermentum nec est. Mauris elementum ex ante pulvinar nisi pretium ut.</p>
<div class="abs read-more">Read More</div>

<h2 class="abs section-title" style="left:670px;top:1192px"><svg width="30" height="34"><use href="#tap"/></svg>What our clients say</h2>
<div class="abs testimonial">
  <p class="quote-text">Victa sunt explicabo. Nemo eni sai th ipsam satal voluptatem quia voluptas sit aspernatur aut odit fugit sed quia consequuntur magni dolores volup tas sit aspernatur aut odit aut fugit.</p>
  <div class="who">– Mira Hollen</div>
  <div class="role">Founder of XYZ Company</div>
  <div class="portrait" role="img" aria-label="Smiling client in a red shirt with arms folded"></div>
</div>

<section class="abs news">
  <h2 class="abs section-title" style="left:100px;top:63px"><svg width="30" height="34"><use href="#tap"/></svg>Latest news</h2>
</section>
<div class="abs view-all">View all</div>

<article class="abs news-card" style="left:93px">
  <span class="mark"></span>
  <h3>12 Tips to clean window</h3>
  <div class="meta">By <span>Admin</span>, &nbsp;Likes <span>23</span></div>
  <p>Neque porro quisquam est, qui thas dolorem ipsum quia dolor sit amets non numquam[...]</p>
  <div class="btn-dark">View details</div>
</article>
<div class="abs news-photo" role="img" aria-label="Plumber fixing pipework under a kitchen sink while a homeowner watches" style="left:339px;background:linear-gradient(160deg,#e9ecef,#bfc6cc 45%,#2b3e6e 80%)"></div>

<article class="abs news-card" style="left:614px">
  <span class="mark"></span>
  <h3>12 Tips to clean window</h3>
  <div class="meta">By <span>Admin</span>, &nbsp;Likes <span>23</span></div>
  <p>Neque porro quisquam est, qui thas dolorem ipsum quia dolor sit amets non numquam[...]</p>
  <div class="btn-dark">View details</div>
</article>
<div class="abs news-photo" role="img" aria-label="Plumber inspecting a white waste pipe under a sink" style="left:861px;background:linear-gradient(150deg,#5a4636,#b08d72 40%,#e8e8e6 70%,#8a8f96)"></div>

<footer class="abs footer"></footer>
<div class="abs foot-col" style="left:101px">
  <h4>Informations</h4><div class="rule"></div>
  <ul><li class="hl">Our Blog</li><li>About Our Shop</li><li>Secure Shopping</li><li>Privacy Policy</li><li>Delivery Informations</li></ul>
</div>
<div class="abs foot-col" style="left:371px">
  <h4>Customer Care</h4><div class="rule"></div>
  <ul><li>Contact Us</li><li>Site Map</li><li>Top Sales &amp; Bestsellers</li><li>Gift Vouchers</li><li>Best Sellers</li></ul>
</div>
<div class="abs foot-col" style="left:676px">
  <h4>Your Account</h4><div class="rule"></div>
  <ul><li>Order Status</li><li>My Wishlist</li><li>Delivery Address</li><li>Order History</li><li>Newsletter</li></ul>
</div>
<div class="abs foot-col" style="left:922px">
  <h4>Get in touch</h4><div class="rule"></div>
  <ul><li>Marlow Trade Shop</li><li>Fern Row 122, Holt Centre</li><li>(011) 555 010 22</li></ul>
</div>
<div class="abs socials" aria-label="Social links"><span></span><span></span><span></span><span></span><span></span><span></span></div>
<div class="abs copyright">Copyright © . All Rights Reserved</div>

</body>
</html>
```